New look and feel for investment website

Hi

Our website needs a crisp and professional look and feel applying to it. Here’s the address: http://www.brightplinth.co.uk. Since posting the brief yesterday (Tuesday, 16 August), we've reduced the amount of content on the home page, which should make life a little easier for you. We will come back later today, with some points of reference in terms of sites we like the look of. (See below)

17 August, 1.20pm GMT. OK, comments generally on the designs submitted so far. Please keep in mind that images of graphs, piles of coins, paper money and pretty females are not what is required. Better to think in terms of abstract imagery instead. Ratios? Circles? Relationships? Patterns? Not money,sex,graphs etc. Hope that helps.

For guidance on look and feel, please refer to these sites, which we like:

http://www.morvelle.co.uk/
http://www.qz.com/
https://www.harrowfieldtamsin.com
https://www.pirelconcerns.com
https://www.kvantule.com
Updates

Here's the Tall Beacons logo created in AI CS5.

Our market is professional financial advisers and relatively sophisticated private investors. The look and feel therefore should be slick and sophisticated - not 'lively' and lightweight, more like a banking site. Please read the brief again where we've added a list of websites that we really like the look of to get a better feel for what we're looking for. Thanks once again, we appreciate the work you're putting in.

It's essential that all the elements that are on the current home page be included on all new designs. 

We use a device in our e-mails which you may wish to incorporate in your design.

Target Market(s)

Professional financial advisers. People who know about investment and money.

Industry/Entity Type

Investment

Requirements
Should not have
• Graphs or people.

```html
<!DOCTYPE html>
<html lang="en">
<head>
<meta charset="utf-8">
<title>Tall Beacons – Value Investing</title>
<link rel="stylesheet" href="https://fonts.googleapis.com/css2?family=Noto+Sans:wght@400&display=swap">
<style>
:root{
  --page-edge:#dde1e8;
  --page-white:#ffffff;
  --text:#4a4a4a;
  --text-soft:#5a5a5a;
  --accent:#f0a000;
  --accent-dark:#e06a00;
  --banner-frame:#c9c9c9;
  --banner-blue:#2b5fc4;
  --box-top:#e4e8ee;
  --box-line:#d6dae0;
}
*{margin:0;padding:0;box-sizing:border-box}
html,body{width:1200px;height:1170px;overflow:hidden}
body{
  font-family:"Noto Sans",Verdana,sans-serif;color:var(--text);
  background:linear-gradient(90deg,var(--page-edge),#f4f5f7 8%,#f4f5f7 92%,var(--page-edge));
  position:relative;
}
.page{position:absolute;left:98px;top:0;width:1004px;height:1170px;background:var(--page-white)}
.abs{position:absolute}
.brand{left:126px;top:26px;font-size:34px;line-height:40px;color:var(--text)}
.top-nav{left:715px;top:15px;font-size:10.5px;letter-spacing:.6px;color:var(--text)}
.top-nav span{margin:0 6px;color:#777}
.register-btn{left:923px;top:38px;width:140px;height:42px;border-radius:3px;
  background:linear-gradient(#ff9a1e,var(--accent-dark));color:#fff;font-size:15px;
  display:flex;align-items:center;justify-content:center;box-shadow:0 3px 3px rgba(0,0,0,.2)}
.banner{left:118px;top:89px;width:964px;height:267px;background:var(--banner-frame);padding:6px 7px}
.banner-inner{position:relative;width:100%;height:100%;
  background:linear-gradient(90deg,#1e4bb6,var(--banner-blue) 40%,#3b73d6)}
.banner-text{position:absolute;left:10px;top:26px;color:#fff;font-size:19.5px;line-height:25px;letter-spacing:.3px}
.banner-text p+p{margin-top:21px}
.banner-art{position:absolute;left:266px;top:0;right:0;bottom:0;
  background:linear-gradient(90deg,rgba(80,110,150,.5),rgba(120,170,220,.55) 40%,rgba(60,110,210,.2) 62%,rgba(240,120,60,.45) 80%,rgba(250,160,120,.5))}
.side-nav{left:118px;top:370px;width:216px;height:350px;border-radius:8px 8px 0 0;
  background:linear-gradient(#dfe3ea,#f6f7f9 60px,#fff);border-right:1px solid #eceef2;list-style:none}
.side-nav li{position:absolute;left:17px;width:195px;font-size:10.5px;line-height:10px;letter-spacing:.6px;color:var(--text)}
.side-nav li::before{content:"›";position:absolute;left:-12px;top:-1px;font-weight:bold}
.intro{left:363px;top:380px;width:705px;font-size:11px;line-height:14.4px;letter-spacing:.5px;color:var(--text-soft)}
.intro .lead{font-size:13.5px;line-height:17px;letter-spacing:.45px;color:var(--text);margin-bottom:19px}
.intro .body{margin-bottom:14px}
.intro .mid{font-size:13.5px;line-height:17px;letter-spacing:.5px;margin:-2px 0 10px}
.intro a{color:var(--accent);text-decoration:none}
.stat{width:225px;height:100px;border:1px solid var(--box-line);border-radius:4px 4px 0 0;
  background:linear-gradient(var(--box-top),#fff 22px,#fff 70%,#eef0f3);
  padding:14px 7px 0;font-size:13px;line-height:17px;letter-spacing:.6px;color:var(--accent)}
.contact-note{left:119px;top:1025px;width:960px;font-size:13.5px;line-height:17px;letter-spacing:.5px;color:var(--text-soft)}
.legal{left:120px;top:1085px;width:955px;font-size:10.6px;line-height:14.4px;letter-spacing:.5px;color:var(--text-soft)}
</style>
</head>
<body>
<div class="page"></div>

<div class="abs brand">Tall Beacons</div>
<nav class="abs top-nav">Login<span>|</span>Register for free<span>|</span>Contact us<span>|</span>Terms &amp; Conditions</nav>
<div class="abs register-btn">Free Registration</div>

<section class="abs banner">
  <div class="banner-inner">
    <div class="banner-art" role="img" aria-label="Banner scene: a house and car on a road before a faint world map, with a hand holding a branching tree of red circles"></div>
    <div class="banner-text">
      <p>A potential return of 23.57 %<br>a year from America’s biggest</p>
      <p>businesses with the emphasis<br>firmly on capital preservation</p>
    </div>
  </div>
</section>

<ul class="abs side-nav">
  <li style="top:15px">Home</li>
  <li style="top:45px">The Two Minute Guide</li>
  <li style="top:75px">Current holdings &amp; year to date results</li>
  <li style="top:105px">What's on the Watch list</li>
  <li style="top:135px">Other important statistics</li>
  <li style="top:165px">About the back testing model and the results</li>
  <li style="top:195px">History of all trades</li>
  <li style="top:225px">Your questions answered</li>
  <li style="top:255px">About our fundamental analysis and the Margin of Safety</li>
  <li style="top:285px">About value investing</li>
  <li style="top:315px">The Halvard 1000 Index and the Crestmoor 500 index</li>
</ul>

<main class="abs intro">
  <p class="lead">A methodical, consistent, highly selective system-driven process for identifying, and investing in, undervalued stocks</p>
  <p class="body">The attractions of value investing need no explanation to those who subscribe to the concept. But it's impractical, if not impossible, for the private investor to implement the strategy (using direct holdings as distinct to collective funds) consistently. Although the data may be available, to undertake fundamental analysis regularly, on a reasonable number of stocks, takes a significant amount of time and effort.</p>
  <p class="body">By definition - and depending on where you look and market conditions - undervalued businesses (stocks) are relatively scarce. So where does the value investor begin their search? Which and how many businesses must be scrutinised before one undervalued entity is found? And having identified a stock that's trading at less than its estimated fair value, will that be the case next week or next month? Fundamentals can change for the worse at any time, so without the benefit of regular analysis, how will the value investor know when to disinvest?</p>
  <p class="mid">Those problems - and others - are now solved: our software takes the hard work out of value investing by providing the quantitative analysis the value investor needs.</p>
  <p class="mid" style="margin-bottom:8px">For more details and the results to date...<a href="#">please go here</a></p>
  <p class="mid" style="margin-bottom:1px">Here's what we do:</p>
  <p class="body">Once a month, month in month out, our program scrutinises the key fundamentals of 1,000 large cap American companies which between them account for 92% of the US securities market.</p>
  <p class="body">First of all, the program sifts through each of the 1,000 stocks searching for favourable arrays of fundamentals: that process usually filters out between 950 and 975 stocks. The software then applies a range of algorithms to the short-listed stocks to identify any which are trading at 35% (or more) below their estimated fair value. There are times when not one single stock on the shortlist satisfies that criteria. But when they do - and if there's room - those stocks are added to our portfolio.</p>
</main>

<div class="abs stat" style="left:118px;top:806px">Average, annualised compound return: 23.57 %</div>
<div class="abs stat" style="left:364px;top:806px">So far this year, the portfolio's return is: 13.49 %</div>
<div class="abs stat" style="left:609px;top:806px;padding-top:12px">Worst ever annual loss: -1.48 %; best ever annual gain: 69.77 %</div>
<div class="abs stat" style="left:857px;top:806px;padding-top:16px">Average return per trade including losing trades: 24.44 %</div>
<div class="abs stat" style="left:118px;top:920px">Maximum number of winning/ losing trades in a row: 11/4</div>
<div class="abs stat" style="left:364px;top:920px;padding-top:15px">Average number of days a stock stays in the portfolio: 287</div>
<div class="abs stat" style="left:609px;top:920px;padding-top:12px">An average of five trades a year and never more than five holdings at any one time</div>
<div class="abs stat" style="left:857px;top:920px;padding-top:16px">86 trades in total, of which 65 were profitable - a success rate of 75.58 %</div>

<p class="abs contact-note">If you have any questions, please e-mail info@tallbeacons.co.uk. Although we’re very willing to answer queries about the way we pick stocks, please do keep in mind that as we’re making this service available free of charge initially, we’re not inclined to expend time and energy debating the relative merits of value investing or fundamental analysis. Other than that, fire away!</p>

<p class="abs legal">This website is published by Tall Beacons Ltd. Registered in England No. 08417326. Registered office: 48 Larchmere Lane London N7 2QT. This website and its content is the copyright of Tall Beacons Ltd - © Tall Beacons Ltd 2011. All rights reserved. Any redistribution or reproduction of part or all of the contents in any form is prohibited other than the following: you may print or download to a local hard disk extracts for your personal and non-commercial use only you may copy the content to individual third parties for their personal use, but only if you acknowledge the website as the source of the material. You may not, except with our express written permission, distribute or commercially exploit the content. Nor may you transmit it or store it in any other website or other form of electronic retrieval system.</p>
</body>
</html>
```